Almadraba Holding Partners - 2018 Website

We are an investment platform based in Madrid, Spain, that focuses on buying companies to improve them operationally and ignite growth through modernization, digitalization and a real hands on approach in the management of those companies we buy. We want to become a serious player in the private equity and money management industry and start approaching more institutional investors (such as pension funds, large family offices, etc.) in the coming months for an intense fundraising campaign.

For such purpose, we need a professional website with an impeccable design and streamlined communication. While we do want to provide some details in terms of what we do, who we are, our investment strategy, etc. we also want to be as vague as possible so that we do not limit ourselves to the claims we do on the website in terms of kind of investments, sectors, industries, geographies, etc. that we work on. For now we raise capital on a deal by deal basis, although our goal is to raise a discretionary pool of capital that we would deploy over 3-5 years. We are now building our track record as a team with already 2 investments which are showing massive growth potential and for which we have been able to execute the investment thesis as planned so far.

We need a simple and clear website with an incredibly professional image to go on the above mentioned roadshow and meet institutional investors.

For reference, we believe the following investment funds have very nice websites:

1) Tordesa Private Equity - http://tordesaequity-example.com/
2) Valdemora Capital - http://www.valdemoracapital-example.es/
3) Quintela Capital - https://www.quintelacapital-example.com/

Thank you in advance.
Tomás Ibáñez Cuesta

Target Market(s)

Potential professional investors - from High Net Worth individuals, to more institutional investors such as Family Offices, Investment Funds, Pension Funds, etc.

Contact Information for Business Card

Name
Title
Contact Details (only for Rafael Sanz Úbeda and Tomás Ibáñez Cuesta)

Coding

Coded - Design and coding required

Number of Pages Required

5+ page

Font styles to use
Sans Serif

Colors

Designer to choose colors to be used in the design.

```html
<!DOCTYPE html>
<html lang="en">
<head>
<meta charset="utf-8">
<title>Almadraba Partners</title>
<link href="https://fonts.googleapis.com/css2?family=Mulish:wght@300;400;600;700&family=Open+Sans:wght@400;600;700;800&display=swap" rel="stylesheet">
<style>
:root{
  --gold:#7a5c22;
  --gold-ring:#8a6a2c;
  --ink:#2b2b2b;
  --text:#555;
  --muted:#6d6d6d;
  --navy:#22263a;
  --footer:#272a33;
  --blog-bg:#f3f5fa;
  --white:#fff;
  --line:#bdbdbd;
}
*{margin:0;padding:0;box-sizing:border-box}
html,body{width:1200px;height:2917px;overflow:hidden}
body{position:relative;background:var(--white);font-family:"Open Sans",Arial,sans-serif;color:var(--text)}
.abs{position:absolute}
.heading{font-family:"Mulish",Arial,sans-serif;font-weight:300;color:var(--ink);letter-spacing:1px}

/* header */
.site-header{left:0;top:0;width:1200px;height:95px;background:var(--white)}
.brand{left:100px;top:24px;display:flex;align-items:center;gap:12px}
.brand-dot{width:40px;height:40px;border-radius:50%;background:var(--navy)}
.brand-name{font-family:"Mulish",sans-serif;font-weight:400;font-size:24px;color:var(--navy);letter-spacing:1px;white-space:nowrap}
.contact-bar{left:538px;top:17px;font-size:14px;color:#333;display:flex;align-items:center;gap:10px;white-space:nowrap}
.contact-bar svg{fill:var(--gold)}
.investor-btn{left:942px;top:8px;width:160px;height:40px;border:2px solid var(--gold);border-radius:20px;font-size:13px;font-weight:600;color:#333;display:flex;align-items:center;justify-content:center;gap:8px;white-space:nowrap}
.main-nav{left:463px;top:61px;display:flex;align-items:center;gap:25px;font-size:13.5px;color:#222;white-space:nowrap}

/* hero */
.hero{left:0;top:95px;width:1200px;height:478px;background:linear-gradient(180deg,#4b5566 0%,#6f6f78 35%,#9c7a64 62%,#4a4340 82%,#2d2a2a 100%)}
.hero-title{left:0;top:210px;width:1200px;text-align:center;font-family:"Mulish",sans-serif;font-weight:300;font-size:74px;color:var(--white);letter-spacing:2px}
.hero-sub{left:0;top:308px;width:1200px;text-align:center;font-size:25px;color:var(--white)}
.quote-btn{left:505px;top:372px;width:190px;height:56px;border:2px solid var(--white);border-radius:28px;color:var(--white);font-weight:700;font-size:16px;display:flex;align-items:center;justify-content:center}
.hero-dots{left:568px;top:518px;display:flex;gap:4px}
.hero-dots span{width:12px;height:12px;border-radius:50%;border:2px solid var(--white)}
.hero-dots span.on{background:var(--white)}

/* welcome */
.welcome-box{left:100px;top:680px;width:660px;height:486px;border:2px solid var(--line)}
.welcome-title{left:140px;top:712px;font-size:36px;line-height:50px}
.welcome-text{left:140px;top:832px;width:500px;font-size:14px;line-height:27px}
.welcome-text p+p{margin-top:27px}
.btn-gold{background:var(--gold);color:var(--white);font-weight:700;font-size:14px;border-radius:24px;display:flex;align-items:center;justify-content:center}
.welcome-btn{left:140px;top:1080px;width:130px;height:47px}
.welcome-photo{left:700px;top:703px;width:401px;height:438px;background:linear-gradient(180deg,#6ea3d8 0%,#8ab7e2 50%,#2d6fae 70%,#1e4f86 100%)}

/* strategy */
.strategy{left:0;top:1272px;width:1200px;height:395px;background:linear-gradient(110deg,#3f3a36 0%,#514b45 55%,#6a655f 100%)}
.strategy-title{left:100px;top:1312px;width:460px;font-size:34px;line-height:50px;color:var(--white)}
.strategy-text{left:100px;top:1430px;width:470px;font-size:14px;line-height:26px;color:var(--white)}
.strategy-btn{left:100px;top:1564px;width:130px;height:47px}
.stat{width:200px;text-align:center;color:var(--white)}
.stat svg{display:block;margin:0 auto}
.stat-label{font-size:14px;line-height:22px;margin-top:8px}

/* values */
.values-title{left:0;top:1752px;width:1200px;text-align:center;font-size:36px}
.values-intro{left:250px;top:1818px;width:700px;text-align:center;font-size:14px;line-height:27px}
.value-card{top:1918px;width:234px;height:240px;border:2px solid var(--line);text-align:center}
.value-card svg{display:block;margin:26px auto 0;fill:var(--gold)}
.value-name{font-family:"Mulish",sans-serif;font-size:18px;color:var(--ink);margin-top:16px;letter-spacing:.5px}
.value-text{font-size:14px;line-height:24px;margin:12px 20px 0}
.slider-arrow{top:2015px;width:40px;height:40px;border:2px solid #888;border-radius:50%;display:flex;align-items:center;justify-content:center}

/* blog */
.blog{left:0;top:2230px;width:1200px;height:473px;background:var(--blog-bg)}
.blog-title{left:0;top:2298px;width:1200px;text-align:center;font-size:36px}
.post-photo{top:2390px;width:218px;height:188px;border:3px solid var(--white);box-shadow:0 0 0 1px #ccc}
.post-title{top:2390px;width:250px;font-family:"Mulish",sans-serif;font-weight:400;font-size:18px;line-height:29px;color:var(--ink)}
.post-meta{top:2456px;font-size:12px;color:#333;display:flex;align-items:center;gap:6px}
.post-meta svg{fill:#333}
.post-excerpt{top:2488px;width:240px;font-size:14px;line-height:26px}

/* footer */
.site-footer{left:0;top:2703px;width:1200px;height:214px;background:var(--footer)}
.social{left:489px;top:2678px;display:flex;gap:10px}
.social span{width:50px;height:50px;border-radius:50%;background:var(--white);border:3px solid var(--footer);display:flex;align-items:center;justify-content:center}
.social .dot{width:12px;height:12px;border-radius:50%;background:var(--footer)}
.footer-contact{left:0;top:2772px;width:1200px;display:flex;justify-content:center;align-items:center;gap:12px;font-size:14px;color:var(--white)}
.footer-contact svg{fill:var(--white)}
.footer-links{left:0;top:2812px;width:1200px;text-align:center;font-size:14px;color:var(--white);word-spacing:3px}
.copyright{left:0;top:2850px;width:1200px;text-align:center;font-size:14px;color:var(--white)}
</style>
</head>
<body>

<header class="abs site-header">
  <div class="abs brand"><span class="brand-dot"></span><span class="brand-name">ALMADRABA PARTNERS</span></div>
  <div class="abs contact-bar">
    <svg width="14" height="14" viewBox="0 0 24 24"><path d="M6.6 10.8a15 15 0 0 0 6.6 6.6l2.2-2.2c.3-.3.7-.4 1-.2 1.1.4 2.3.6 3.6.6.6 0 1 .4 1 1V20c0 .6-.4 1-1 1A17 17 0 0 1 3 4c0-.6.4-1 1-1h3.5c.6 0 1 .4 1 1 0 1.3.2 2.5.6 3.6.1.3 0 .7-.2 1z"/></svg>
    <span>+34 91 000 12 34</span><span>|</span>
    <svg width="15" height="12" viewBox="0 0 24 18"><path d="M0 0h24v2L12 10 0 2zM0 4l12 8 12-8v14H0z"/></svg>
    <span>info@almadraba-example.com</span>
  </div>
  <div class="abs investor-btn">
    <svg width="12" height="13" viewBox="0 0 24 26" fill="#7a5c22"><circle cx="12" cy="7" r="6"/><path d="M0 26c0-8 5-12 12-12s12 4 12 12z"/></svg>
    INVESTOR ACCESS
  </div>
  <nav class="abs main-nav">
    <span>HOME</span><span>ABOUT US</span><span>SERVICES</span><span>BUSINESSES</span><span>BLOG</span><span>CAREER</span><span>CONTACT US</span>
    <svg width="14" height="14" viewBox="0 0 24 24" fill="none" stroke="#222" stroke-width="3"><circle cx="10" cy="10" r="7"/><path d="M15 15l7 7"/></svg>
  </nav>
</header>

<section class="abs hero" role="img" aria-label="Madrid skyline with business towers at sunset"></section>
<h1 class="abs hero-title">ALMADRABA PARTNERS</h1>
<p class="abs hero-sub">We are an investment platform based in Madrid, Spain</p>
<div class="abs quote-btn">GET A QUOTE</div>
<div class="abs hero-dots"><span class="on"></span><span></span><span></span><span></span></div>

<div class="abs welcome-box"></div>
<h2 class="abs heading welcome-title">WELCOME TO<br>ALMADRABA PARTNERS</h2>
<div class="abs welcome-text">
  <p>Almadraba Holding Partners is a unique investment platform focused on value creation through consolidation, digitalization and internationalization of large, fragmented and traditional sectors. We build platforms and ecosystems, and ignite organic and inorganic growth in plateauing industries</p>
  <p>We do so by applying a true hands-on approach and deep involvement in operations throughout the life of the investment, and by rigorously analysing the sectors we invest in.</p>
</div>
<div class="abs btn-gold welcome-btn">READ MORE</div>
<div class="abs welcome-photo" role="img" aria-label="Sailboats racing on the open sea"></div>

<section class="abs strategy" role="img" aria-label="Hands working on documents and a laptop at a desk"></section>
<h2 class="abs heading strategy-title">ALMADRABA HOLDING<br>PARTNERS STRATEGY</h2>
<p class="abs strategy-text">We provide exit and continuity solutions focused on growth for family-owned businesses in Spain, which will need to transition to professional management, to go under consolidation to grow and compete globally and to expand their geographical horizons,..</p>
<div class="abs btn-gold strategy-btn">READ MORE</div>

<div class="abs stat" style="left:577px;top:1342px">
  <svg width="140" height="140" viewBox="0 0 140 140"><circle cx="70" cy="70" r="66" fill="none" stroke="var(--gold-ring)" stroke-width="4"/><circle cx="70" cy="70" r="66" fill="none" stroke="#fff" stroke-width="4" stroke-dasharray="104 311" transform="rotate(-90 70 70)"/><text x="70" y="84" text-anchor="middle" font-family="Open Sans,sans-serif" font-weight="800" font-size="40" fill="#fff">85%</text></svg>
  <div class="stat-label">Of Spanish businesses<br>are categorized as<br>family-owned</div>
</div>
<div class="abs stat" style="left:755px;top:1342px">
  <svg width="140" height="140" viewBox="0 0 140 140"><circle cx="70" cy="70" r="66" fill="none" stroke="var(--gold-ring)" stroke-width="4"/><circle cx="70" cy="70" r="66" fill="none" stroke="#fff" stroke-width="4" stroke-dasharray="80 335" transform="rotate(-90 70 70)"/><text x="70" y="84" text-anchor="middle" font-family="Open Sans,sans-serif" font-weight="800" font-size="40" fill="#fff">70%</text></svg>
  <div class="stat-label">Contribution to Spain's<br>GDP by family-owned<br>businesses</div>
</div>
<div class="abs stat" style="left:930px;top:1342px">
  <svg width="140" height="140" viewBox="0 0 140 140"><circle cx="70" cy="70" r="66" fill="none" stroke="var(--gold-ring)" stroke-width="4"/><circle cx="70" cy="70" r="66" fill="none" stroke="#fff" stroke-width="4" stroke-dasharray="130 285" transform="rotate(180 70 70)"/><text x="70" y="84" text-anchor="middle" font-family="Open Sans,sans-serif" font-weight="800" font-size="40" fill="#fff">70%</text></svg>
  <div class="stat-label">Of private employment<br>generated by family<br>businesses</div>
</div>

<h2 class="abs heading values-title">OUR VALUES</h2>
<p class="abs values-intro">Almadraba Holding Partners and its founders, as well as its co-investors, have conducted business with immaculate reputation for decades in different regions of the world.</p>

<div class="abs slider-arrow" style="left:30px"><svg width="12" height="14" viewBox="0 0 12 14" fill="none" stroke="#555" stroke-width="2"><path d="M9 1L3 7l6 6"/></svg></div>
<div class="abs slider-arrow" style="left:1130px"><svg width="12" height="14" viewBox="0 0 12 14" fill="none" stroke="#555" stroke-width="2"><path d="M3 1l6 6-6 6"/></svg></div>

<div class="abs value-card" style="left:100px">
  <svg width="44" height="44" viewBox="0 0 24 24"><rect x="1" y="10" width="5" height="12"/><path d="M8 10l5-8c2 0 3 1 2.5 3L14 9h7c1.5 0 2.5 1.3 2 2.7l-2.5 8.5c-.3 1-1.2 1.8-2.3 1.8H8z"/></svg>
  <div class="value-name">EXCELLENCE</div>
  <p class="value-text">As such, they are extremely concerned about preserving the Group's reputation</p>
</div>
<div class="abs value-card" style="left:355px">
  <svg width="60" height="44" viewBox="0 0 30 22"><path d="M0 5h22V1l8 6-8 6V9H0zM30 15H8v-4l-8 6 8 6v-4h22z"/></svg>
  <div class="value-name">INTEGRITY</div>
  <p class="value-text">As such, they are extremely concerned about preserving the Group's reputation</p>
</div>
<div class="abs value-card" style="left:611px">
  <svg width="50" height="44" viewBox="0 0 28 24"><circle cx="10" cy="14" r="7"/><circle cx="10" cy="14" r="2.5" fill="#fff"/><circle cx="21" cy="6" r="5"/><circle cx="21" cy="6" r="1.8" fill="#fff"/><circle cx="22" cy="19" r="4"/><circle cx="22" cy="19" r="1.4" fill="#fff"/></svg>
  <div class="value-name">HIGH PERFORMANCE</div>
  <p class="value-text">As such, they are extremely concerned about preserving the Group's reputation</p>
</div>
<div class="abs value-card" style="left:866px">
  <svg width="50" height="44" viewBox="0 0 30 26"><circle cx="15" cy="6" r="5"/><circle cx="5" cy="9" r="3.5"/><circle cx="25" cy="9" r="3.5"/><path d="M7 26c0-8 3-12 8-12s8 4 8 12zM0 22c0-6 2-9 6-9l2 1c-1.5 2-2 5-2 8zM30 22c0-6-2-9-6-9l-2 1c1.5 2 2 5 2 8z"/></svg>
  <div class="value-name">TEAMWORK</div>
  <p class="value-text">As such, they are extremely concerned about preserving the Group's reputation</p>
</div>

<section class="abs blog"></section>
<h2 class="abs heading blog-title">LATEST BLOG</h2>

<div class="abs post-photo" style="left:100px;background:linear-gradient(135deg,#8aa0b8,#e4e8ee 55%,#c9d4de)" role="img" aria-label="Person reviewing financial charts on paper"></div>
<h3 class="abs post-title" style="left:342px">At vero eos et accusamus et iusto odio dignissimos</h3>
<div class="abs post-meta" style="left:342px"><svg width="11" height="11" viewBox="0 0 24 24"><path d="M2 5h20v17H2zM6 1h3v5H6zm9 0h3v5h-3z"/></svg><span>17/08/2017</span><span>|</span><svg width="11" height="11" viewBox="0 0 24 26"><circle cx="12" cy="7" r="6"/><path d="M0 26c0-8 5-12 12-12s12 4 12 12z"/></svg><span>John Doe</span></div>
<p class="abs post-excerpt" style="left:342px">Et harum quidem rerum facilis est et expedita distinctio ibero tepore cum soluta nobis est..</p>

<div class="abs post-photo" style="left:617px;background:linear-gradient(135deg,#5a5048,#b59a86 50%,#ece9e6)" role="img" aria-label="Hands using a tablet with business charts"></div>
<h3 class="abs post-title" style="left:862px">At vero eos et accusamus et iusto odio dignissimos</h3>
<div class="abs post-meta" style="left:862px"><svg width="11" height="11" viewBox="0 0 24 24"><path d="M2 5h20v17H2zM6 1h3v5H6zm9 0h3v5h-3z"/></svg><span>17/08/2017</span><span>|</span><svg width="11" height="11" viewBox="0 0 24 26"><circle cx="12" cy="7" r="6"/><path d="M0 26c0-8 5-12 12-12s12 4 12 12z"/></svg><span>John Doe</span></div>
<p class="abs post-excerpt" style="left:862px">Et harum quidem rerum facilis est et expedita distinctio ibero tepore cum soluta nobis est..</p>

<footer class="abs site-footer"></footer>
<div class="abs social" aria-label="Social links">
  <span><i class="dot"></i></span><span><i class="dot"></i></span><span><i class="dot"></i></span>
  <span><svg width="18" height="14" viewBox="0 0 24 18" fill="#272a33"><path d="M0 0h24v2L12 10 0 2zM0 4l12 8 12-8v14H0z"/></svg></span>
</div>
<div class="abs footer-contact">
  <svg width="11" height="15" viewBox="0 0 16 22"><path d="M8 0a8 8 0 0 0-8 8c0 6 8 14 8 14s8-8 8-14a8 8 0 0 0-8-8zm0 11a3 3 0 1 1 0-6 3 3 0 0 1 0 6z"/></svg>
  <span>C/ Ejemplo 12, bajo 28001 Madrid</span><span>|</span>
  <svg width="14" height="14" viewBox="0 0 24 24"><path d="M6.6 10.8a15 15 0 0 0 6.6 6.6l2.2-2.2c.3-.3.7-.4 1-.2 1.1.4 2.3.6 3.6.6.6 0 1 .4 1 1V20c0 .6-.4 1-1 1A17 17 0 0 1 3 4c0-.6.4-1 1-1h3.5c.6 0 1 .4 1 1 0 1.3.2 2.5.6 3.6.1.3 0 .7-.2 1z"/></svg>
  <span>+34 91 000 12 34</span><span>|</span>
  <svg width="15" height="12" viewBox="0 0 24 18"><path d="M0 0h24v2L12 10 0 2zM0 4l12 8 12-8v14H0z"/></svg>
  <span>info@almadraba-example.com</span>
</div>
<p class="abs footer-links">Help | FAQ | Support | Sitemap | Terms Of Use | Privacy Statement</p>
<p class="abs copyright">Copyrights © 2018, Almadraba Partners. All rights reserved.</p>

</body>
</html>
```